I need to design a business card
on the front side the words "VELTRIS CAPITAL" with the top half surrounded by a stylised cloud. Minimalist, navy blue font on white background, with the Veltris capital in embossing.

On the back contact details (avoid centered). I would rather have the details taking the 2/3rd on the right and having the logo on the left, but anyway not plain centered

Marcello Lo Ruffo
CEO e Fondatore

m.loruffo@veltris-capital.example
+39.328.514.6082

Piazza Ventrano 7
20135 Milano

```html
<!DOCTYPE html>
<html lang="it">
<head>
<meta charset="utf-8">
<title>Veltris Capital – Biglietto da visita</title>
<link rel="stylesheet" href="https://fonts.googleapis.com/css2?family=Arimo:wght@400;700&display=swap">
<style>
  :root {
    --paper: #ffffff;
    --ink: #3b4046;
    --ink-soft: #4a4e53;
    --icon: #34383d;
    --rule: #4a4e53;
  }
  html, body {
    margin: 0;
    padding: 0;
    overflow: hidden;
    background: var(--paper);
  }
  .card {
    position: relative;
    width: 1200px;
    height: 801px;
    background: var(--paper);
    font-family: "Arimo", Arial, sans-serif;
    color: var(--ink-soft);
    overflow: hidden;
  }
  .brand {
    position: absolute;
    left: 105px;
    top: 316px;
    width: 390px;
    text-align: center;
    font-size: 40px;
    font-weight: 400;
    line-height: 40px;
    color: var(--ink);
  }
  .divider {
    position: absolute;
    left: 566px;
    top: 174px;
    width: 2px;
    height: 432px;
    background: var(--rule);
  }
  .icon {
    position: absolute;
    left: 594px;
    width: 30px;
    height: 30px;
  }
  .text {
    position: absolute;
    left: 651px;
    white-space: nowrap;
    line-height: 1;
  }
  .person__name {
    font-size: 48px;
    font-weight: 700;
    color: var(--ink);
  }
  .person__role { font-size: 31px; }
  .detail { font-size: 32px; }
  .address {
    font-size: 32px;
    line-height: 45px;
  }
</style>
</head>
<body>
<main class="card">
  <div class="brand">Veltris Capital</div>

  <div class="divider"></div>

  <svg class="icon" style="top:225px" viewBox="0 0 30 30" aria-hidden="true">
    <circle cx="15" cy="15" r="15" fill="var(--icon)"/>
    <circle cx="15" cy="11.5" r="5" fill="#fff"/>
    <path d="M6 24c2-5 5.5-6.5 9-6.5s7 1.5 9 6.5a13 13 0 0 1-18 0z" fill="#fff"/>
  </svg>
  <div class="text person__name" style="top:216px">Marcello Lo Ruffo</div>
  <div class="text person__role" style="top:285px">CEO e Fondatore</div>

  <svg class="icon" style="top:372px" viewBox="0 0 30 30" aria-hidden="true">
    <circle cx="15" cy="15" r="15" fill="var(--icon)"/>
    <g fill="none" stroke="#fff" stroke-width="2">
      <circle cx="15" cy="15" r="9"/>
      <ellipse cx="15" cy="15" rx="4" ry="9"/>
      <line x1="6" y1="15" x2="24" y2="15"/>
    </g>
  </svg>
  <div class="text detail" style="top:371px">m.loruffo@veltris-capital.example</div>

  <svg class="icon" style="top:417px" viewBox="0 0 30 30" aria-hidden="true">
    <circle cx="15" cy="15" r="15" fill="var(--icon)"/>
    <path d="M10 7.5l3 3.5-2 2.2c1.2 2.6 3.2 4.6 5.8 5.8l2.2-2 3.5 3-1.8 3c-6.5-.5-12.2-6.2-12.7-12.7z" fill="#fff"/>
  </svg>
  <div class="text detail" style="top:416px">+39.328.514.6082</div>

  <svg class="icon" style="top:507px" viewBox="0 0 30 30" aria-hidden="true">
    <circle cx="15" cy="15" r="15" fill="var(--icon)"/>
    <path d="M15 7l8 7h-2.5v8h-4v-5h-3v5h-4v-8H7z" fill="#fff"/>
  </svg>
  <div class="text address" style="top:500px">
    Piazza Ventrano 7<br>
    20135 Milano
  </div>
</main>
</body>
</html>
```